Hardcore nerd needs to stand out in a sea of dull Defence business cards

Wombat Devices is a new Australian consulting engineering company that turns research and theory into practical systems. No evangelistic fluff, just mathematics and physics into electronic and optical circuits for consumer products, scientific research or Defence applications.

We already have a recognised logo (provided) which is often dark blue/black on a light background but we're open to other combinations. (Us engineers tend to have limited aesthetic imagination :)

Some of our recent products have included:
* Instrumentation for electrical testing,
* Radar jammers,
* GPS antenna design,
* Satellite tracking systems,
* High power lasers

We're open to both single and double-sided designs - happy to be convinced either way.

P.S. Another group is working on the web page, so - alas - our web site is currently of no use for images/ideas...

Target Market(s)

Engineering managers,
Scientists

Contact Information for Business Card

Dr Colin Marsh
R&D Engineer

colin@wombatdevicesco.com.au
0427 563 210

PO Box XXX (to be confirmed)
Banks ACT 2913
Australia

Font styles to use
Serif
Sans Serif

Colors

Designer to choose colors to be used in the design.

Requirements
Must have
• My contact details!
• I've had many (great) "bold and plain" designs submitted already, so feel free to be artistically creative :)
• Happy to take advice re fonts/colours/printability etc.
Nice to have
• I'm not sure if "lists" are more at home on a CV than a business card, but representative services include:
• Applied electromagnetics
• RF and high speed electronics
• Signal and image processing
• Electro-optical and laser systems
• Concept-to-prototype design services
• If you're considering double sided cards, then often measuring/alignment grids/rulers feature on the back of similar cards.
• e.g. https://www.lumoptix-example.com/newgrouppage9.cfm?objectgroup_id=4815
• https://www.lumoptix-example.com/newgrouppage9.cfm?objectgroup_ID=4817
• ..or even a "Smith chart" (google will return lots)
• Generic images to represent a capability might work - googling images associated with keyword for each of these areas might help:
• - "passive radar", "phased array", "fdtd", "vircator"
• RF and high speed electronic design
• - "smith chart", "microstrip circuits", "dimensioned drawing", "electronic schematic"
• - "dft", "iir filter"
• - "optical cavity". "laser energy level diagram"
• Background/watermarked images outlines/wireframes/schematics would probably look OK.
Should not have
• If a list of projects/services is provided, it is important not to make the client feel that this is "all" the company can do. Engineering design is a creative discipline (like graphics :)
• Please, no stock "military" snaps like planes, missiles, etc!

```html
<!DOCTYPE html>
<html lang="en">
<head>
<meta charset="utf-8">
<title>Wombat Devices — Business Card</title>
<link href="https://fonts.googleapis.com/css2?family=EB+Garamond:wght@400;500&display=swap" rel="stylesheet">
<style>
  :root {
    --stage: #e9e7e3;
    --card-white: #fbfbfb;
    --card-black: #1c1c1d;
    --accent-blue: #2fa4dc;
    --ink: #3a3a3a;
    --ink-soft: #6a6a6a;
    --emblem-faint: #262627;
  }
  * { box-sizing: border-box; margin: 0; padding: 0; }
  html, body {
    width: 1200px; height: 800px; overflow: hidden;
    background: var(--stage);
    font-family: "EB Garamond", Georgia, serif;
  }
  .stage {
    width: 1200px; height: 800px;
    display: flex; align-items: center; justify-content: center; gap: 60px;
  }
  .card {
    position: relative;
    width: 525px; height: 300px;
    box-shadow: 0 6px 18px rgba(0,0,0,0.18);
    overflow: hidden;
  }
  /* Front */
  .card--front { background: var(--card-white); color: var(--ink); }
  .card__identity {
    position: absolute; top: 34px; right: 36px; text-align: right;
  }
  .card__name {
    font-size: 27px; font-weight: 400; letter-spacing: 0.5px;
    color: var(--accent-blue); text-transform: uppercase;
  }
  .card__role { font-size: 12px; color: var(--ink-soft); margin-top: 4px; }
  .card__contacts {
    position: absolute; right: 36px; top: 128px;
    list-style: none; text-align: right; font-size: 12.5px; line-height: 1;
  }
  .card__contacts li {
    display: flex; align-items: center; justify-content: flex-end; gap: 10px;
    margin-bottom: 12px;
  }
  .contact-icon {
    width: 16px; height: 16px; background: var(--accent-blue);
    display: inline-flex; align-items: center; justify-content: center;
  }
  .card__address {
    position: absolute; left: 36px; bottom: 32px;
    font-size: 12.5px; line-height: 1.45; color: var(--ink);
  }
  /* Back */
  .card--back { background: var(--card-black); }
  .card__emblem-faint {
    position: absolute; left: 150px; top: 170px;
    width: 230px; height: 230px; border-radius: 50%;
    background: var(--emblem-faint);
  }
  .card__brand {
    position: absolute; left: 0; right: 0; top: 118px;
    display: flex; align-items: center; justify-content: center; gap: 14px;
  }
  .brand-dot {
    width: 40px; height: 40px; border-radius: 50%; background: var(--accent-blue);
  }
  .brand-name {
    font-size: 34px; font-weight: 500; color: var(--accent-blue);
    text-transform: uppercase; letter-spacing: 1.5px;
  }
</style>
</head>
<body>
<main class="stage">
  <section class="card card--front" aria-label="Business card front">
    <div class="card__identity">
      <h1 class="card__name">Dr Colin Marsh</h1>
      <p class="card__role">R&amp;D Engineer</p>
    </div>
    <ul class="card__contacts">
      <li>colin@wombatdevicesco.com.au
        <span class="contact-icon" aria-hidden="true">
          <svg width="10" height="8" viewBox="0 0 10 8"><rect x="0.5" y="0.5" width="9" height="7" fill="none" stroke="#fff"/><path d="M0.5 0.5 L5 4.5 L9.5 0.5" fill="none" stroke="#fff"/></svg>
        </span>
      </li>
      <li>0427 563 210
        <span class="contact-icon" aria-hidden="true">
          <svg width="8" height="11" viewBox="0 0 8 11"><rect x="0.5" y="0.5" width="7" height="10" rx="1" fill="none" stroke="#fff"/><circle cx="4" cy="8.5" r="0.8" fill="#fff"/></svg>
        </span>
      </li>
    </ul>
    <address class="card__address" style="font-style:normal">
      PO Box XXX, Banks ACT 2913,<br>Australia
    </address>
  </section>

  <section class="card card--back" aria-label="Business card back">
    <div class="card__emblem-faint" role="img" aria-label="Faint large emblem decoration"></div>
    <div class="card__brand">
      <span class="brand-dot" aria-hidden="true"></span>
      <span class="brand-name">Wombat Devices</span>
    </div>
  </section>
</main>
</body>
</html>
```